WEBSITE REFRESH / REDESIGN- USE OLD WEBSITE TO CONSTRUCT NEW TEMPLATE

The current website was designed years ago, and we is now outdated.

We are looking for an updated design to our old website. We are looking for something that is consumer friendly, shows sophistication and is pleasing to the eye and modern.

Our old website consists of 25 pages. You are not required to design new text other from copying and pasting the current text and images.

The redesign requires the site to be modern, easy to navigate.

The current website is: www.brovelwood.com.au, every page must be included and titled the same as the old one.

The home page requires a large slider, that I can change easily often.

Any new ideas are welcome.

I do have a template that I have purchased, however this isn't required to be used....any new exciting ideas will be considered.

Target Market(s)

existing customers; new customers demonstrating what we are offering to sell

Coding

Font styles to use
Sans Serif

Colors
85cae6
33a6d7
0293ce
86cfc6
33b8a4
add136
fbee3e
fbf289
faa54b

Requirements
Must have
• text and photos from existing site. every page needs to be included in redesign.

```html
<!DOCTYPE html>
<html lang="en">
<head>
<meta charset="utf-8">
<title>Quote Request – Brovelwood Timber</title>
<link rel="stylesheet" href="https://fonts.googleapis.com/css2?family=Montserrat:wght@400;500;600;700&display=swap">
<style>
:root{
  --sky:#85cae6;
  --blue:#33a6d7;
  --blue-deep:#0293ce;
  --mint:#86cfc6;
  --teal:#33b8a4;
  --lime:#add136;
  --sun:#fbee3e;
  --sun-soft:#fbf289;
  --orange:#faa54b;
  --ink:#2f3a40;
  --body:#6b7378;
  --footer:#243038;
  --footer-base:#1b252b;
  --footer-rule:#36444d;
  --white:#ffffff;
}
*{box-sizing:border-box;margin:0;padding:0}
html,body{width:1006px;height:1200px;overflow:hidden}
body{position:relative;background:var(--white);font-family:'Montserrat',sans-serif;color:var(--body)}
.abs{position:absolute}

.topbar{left:0;top:0;width:1006px;height:33px;background:var(--blue-deep);color:var(--white);font-size:10.5px;letter-spacing:-.2px}
.topbar .info{left:27px;top:10px;display:flex;gap:10px;align-items:center;white-space:nowrap}
.topbar .info span{display:flex;align-items:center;gap:5px}
.social{display:flex;gap:14px}
.social i{display:block;width:10px;height:10px;border-radius:50%;background:var(--white)}
.topbar .social{right:38px;top:12px}

.header{left:0;top:33px;width:1006px;height:65px;background:var(--white);box-shadow:0 2px 6px rgba(2,147,206,.12)}
.brand{font-weight:700;font-size:17px;color:var(--blue-deep);letter-spacing:.5px;display:flex;align-items:center;gap:7px}
.header .brand{left:19px;top:22px}
.brand b{display:block;width:12px;height:12px;border-radius:50%;background:var(--lime)}
.nav a{position:absolute;top:27px;font-size:11px;font-weight:600;letter-spacing:1px;color:var(--ink);text-decoration:none;white-space:nowrap}
.nav a.active{color:var(--blue-deep)}
.nav-marker{left:728px;top:98px;width:0;height:0;border-left:8px solid transparent;border-right:8px solid transparent;border-top:8px solid var(--white);z-index:2}

.hero{left:0;top:98px;width:1006px;height:188px;background:linear-gradient(100deg,var(--blue-deep) 0%,var(--blue) 100%);overflow:hidden}
.hero .folder{left:0;top:0;width:338px;height:188px;background:linear-gradient(135deg,var(--sky),var(--blue))}
.hero .tile{top:18px;height:74px;border-radius:4px;background:linear-gradient(160deg,rgba(133,202,230,.55),rgba(51,166,215,.35))}
.hero .stripe{left:0;bottom:0;width:1006px;height:5px;background:linear-gradient(90deg,var(--teal),var(--lime),var(--sun),var(--orange))}
.hero h1{left:0;top:68px;width:992px;text-align:center;font-weight:500;font-size:46px;letter-spacing:1.5px;color:var(--white)}

.intro{left:54px;top:333px;width:880px;font-size:12px;line-height:26px;color:var(--body)}
.intro p{margin-bottom:15px}

.option{text-align:center;width:320px}
.option h3{font-weight:600;font-size:12.5px;color:var(--teal)}
.option p{font-size:12px;color:var(--body);margin-top:12px}
.photo{position:absolute;border-radius:6px}

.totop{left:913px;top:467px;width:36px;height:27px;background:var(--teal);border-radius:4px;display:flex;align-items:center;justify-content:center}

.footer-rule{left:0;top:800px;width:1006px;height:9px;background:linear-gradient(90deg,var(--blue-deep),var(--blue),var(--teal),var(--lime))}
.footer{left:0;top:809px;width:1006px;height:328px;background:var(--footer);color:var(--white)}
.footer .brand{left:49px;top:69px;color:var(--white)}
.service{left:49px;top:139px;width:300px;font-size:12px;line-height:26px}
.footer h4{position:absolute;top:61px;font-size:11.5px;font-weight:700;letter-spacing:.2px;color:var(--sun)}
.links{left:354px;top:97px;width:284px;list-style:none}
.links li{height:41.6px;border-bottom:1px solid var(--footer-rule);font-size:12px;padding-top:8px}
.links li.active{color:var(--sky)}
.contact{left:661px;top:103px;font-size:12px;line-height:25px}
.contact .gap{margin-top:12px}

.base{left:0;top:1137px;width:1006px;height:63px;background:var(--footer-base);color:var(--white)}
.base .legal{left:49px;top:17px;font-size:8.5px;font-weight:600;line-height:19px;letter-spacing:-.2px}
.base .social{left:906px;top:31px}
.base .social i{background:var(--sky)}
</style>
</head>
<body>

<div class="abs topbar">
  <div class="abs info">
    <span><svg width="9" height="8" viewBox="0 0 9 8"><rect x=".5" y=".5" width="8" height="7" fill="none" stroke="#fff"/><path d="M.5 .5 4.5 4.5 8.5 .5" fill="none" stroke="#fff"/></svg>info@brovelwood.com</span>
    <span><svg width="8" height="8" viewBox="0 0 8 8"><path d="M1 0h2l1 2-1.2 1a5 5 0 0 0 2.2 2.2L6 4l2 1v2a1 1 0 0 1-1 1A7 7 0 0 1 0 1a1 1 0 0 1 1-1z" fill="#fff"/></svg>(03) 9000-4821</span>
    <span><svg width="9" height="9" viewBox="0 0 9 9"><circle cx="4.5" cy="4.5" r="3.8" fill="none" stroke="#fff"/><path d="M4.5 2v2.7h2" fill="none" stroke="#fff"/></svg>Mon - Thur 7:00am to 4.30pm Friday 7:00am to 4.00pm Saturday 8am to 11am</span>
  </div>
  <div class="abs social"><i></i><i></i></div>
</div>

<div class="abs header">
  <div class="abs brand"><b></b>BROVELWOOD</div>
  <nav class="nav">
    <a style="left:510px">HOME</a>
    <a style="left:582px">PRODUCTS</a>
    <a class="active" style="left:684px">QUOTE REQUEST</a>
    <a style="left:822px">SPECIALS</a>
    <a style="left:915px">CONTACT</a>
  </nav>
</div>
<div class="abs nav-marker"></div>

<section class="abs hero">
  <div class="abs folder" role="img" aria-label="Printed quote form in an open folder"></div>
  <div class="abs tile" style="left:386px;width:108px" role="img" aria-label="Stacked timber boards"></div>
  <div class="abs tile" style="left:509px;width:109px" role="img" aria-label="Stacked timber boards"></div>
  <div class="abs tile" style="left:631px;width:114px" role="img" aria-label="Stacked timber boards"></div>
  <h1 class="abs">Quote Request</h1>
  <div class="abs stripe"></div>
</section>

<div class="abs intro">
  <p>We are more then happy to quote you on any timber materials you require. You can request a quote by email, phone, or online using our online quote request.</p>
  <p>We are also happy to help you find a fencer to build your next fence.</p>
  <p>Please choose from one of the following below:</p>
</div>

<div class="abs option" style="left:106px;top:509px">
  <h3>Fencing Material Quote</h3>
  <p>Quotes for timber materials.</p>
</div>
<div class="photo" style="left:130px;top:554px;width:272px;height:178px;background:linear-gradient(120deg,#8a5a3e,#8d7a5e 45%,#a69a82)" role="img" aria-label="Stacks of treated and hardwood fencing timber"></div>

<div class="abs option" style="left:566px;top:486px">
  <h3>Find A Fencer</h3>
  <p>To request a fencers phone number.</p>
</div>
<div class="photo" style="left:610px;top:532px;width:234px;height:160px;background:linear-gradient(90deg,#5c6478 0,#6f6557 22%,#a58b6c 40%,#b49a7a)" role="img" aria-label="Fencer building a timber paling fence"></div>

<div class="abs totop"><svg width="10" height="6" viewBox="0 0 10 6"><path d="M1 5 5 1l4 4" fill="none" stroke="#fff" stroke-width="1.5"/></svg></div>

<div class="abs footer-rule"></div>
<footer class="abs footer">
  <div class="abs brand"><b></b>BROVELWOOD</div>
  <p class="abs service">We service: Deer Park, Ravenhall, Sunshine, Sunshine North, Footscray, Yarraville, Taylors Lakes, Keilor, Sydenham, Melton, Gisborne, Sunbury, Laverton, Point Cook, Werribee, Epping and many other suburbs.</p>
  <h4 style="left:354px">QUICK LINKS</h4>
  <ul class="abs links">
    <li>› Products</li>
    <li>› Specials</li>
    <li class="active">› Quote Request</li>
    <li>› Contact</li>
  </ul>
  <h4 style="left:661px">CONTACT US</h4>
  <div class="abs contact">
    <div>7 Ashgrove Drive,</div>
    <div>Deer Park (Ravenhall) VIC 3023</div>
    <div class="gap">Phone: (03) 9000-4821</div>
    <div>E-mail: info@brovelwood.com</div>
  </div>
</footer>

<div class="abs base">
  <div class="abs legal">COPYRIGHT 2018 - 2019 BROVELWOOD TIMBER ALL RIGHTS RESERVED PRIVACY POLICY | PTERMS AND CONIDTIONS<br>www.brovelwood.com.au | www.brovelwoodsupplies.com.au</div>
  <div class="abs social"><i></i><i></i></div>
</div>

</body>
</html>
```